Harbourline Wellness Clinic website

Design a SEO friendly website

Target Market(s)

Adults with health challenges

Coding

Coded - Design and coding required

Number of Pages Required

5+ page

Requirements
Must have
• Free consultation form link to email response.
Information to be taken from our respective equipment suppliers websites as per file attached.

```html
<!DOCTYPE html>
<html lang="en">
<head>
<meta charset="utf-8">
<title>Harbourline Wellness Clinic – Doctors, FAQ &amp; Gallery</title>
<link href="https://fonts.googleapis.com/css2?family=Raleway:wght@600;700&family=Open+Sans:wght@400;600&display=swap" rel="stylesheet">
<style>
:root{
  --navy:#2c4964;
  --blue:#1977cc;
  --soft-blue:#f1f6fd;
  --icon:#a0b9d6;
  --text:#444444;
  --muted:#6b7b8c;
  --line:#dde3ea;
  --white:#ffffff;
}
*{margin:0;padding:0;box-sizing:border-box}
html,body{width:927px;height:1200px;overflow:hidden;background:var(--white)}
body{position:relative;font-family:"Open Sans",sans-serif;color:var(--text)}
.abs{position:absolute}
.service-link{left:151px;font-size:8.5px;color:var(--navy)}
.service-divider{left:293px;top:30px;width:1px;height:56px;background:var(--line)}
.top-rule{left:633px;top:30px;width:144px;height:3px;background:linear-gradient(90deg,#eef1f5,#f3e9ee,#eef1f5)}
.section-title{left:0;width:927px;text-align:center;font-family:"Raleway",sans-serif;font-weight:700;color:var(--navy)}
.title-rule{left:430px;width:67px;height:1px;background:var(--line)}
.title-rule::after{content:"";position:absolute;left:22px;top:-1px;width:22px;height:2px;background:var(--blue)}
.section-sub{left:0;width:927px;text-align:center;font-size:8px;color:var(--muted)}
.doctor-card{width:304px;height:134px;background:var(--white);border-radius:4px;box-shadow:0 2px 12px rgba(44,73,100,.09)}
.doctor-photo{position:absolute;left:17px;top:17px;width:102px;height:102px;border-radius:50%}
.doctor-info{position:absolute;left:136px;top:17px}
.doctor-name{font-family:"Raleway",sans-serif;font-weight:700;font-size:11.5px;color:var(--navy)}
.doctor-role{font-size:8px;color:var(--muted);margin-top:3px;height:11px}
.doctor-rule{width:28px;height:1px;background:#b2c8dd;margin-top:6px}
.doctor-note{font-size:7px;color:var(--muted);margin-top:4px;height:10px}
.social{display:flex;gap:5px;margin-top:6px}
.social span{width:18px;height:18px;border-radius:50%;background:var(--icon)}
.faq-band{left:30px;top:546px;width:867px;height:384px;background:var(--soft-blue)}
.faq-item{left:207px;width:513px;background:var(--white);border-radius:2px}
.faq-q{position:absolute;left:12px;top:12px;display:flex;align-items:center;gap:5px;font-size:8.5px;color:var(--text)}
.faq-item.open .faq-q{color:var(--blue)}
.faq-a{position:absolute;left:12px;top:34px;font-size:7.5px;color:var(--muted)}
.chev{position:absolute;right:14px;top:14px}
.gallery-shot{top:1039px;height:130px}
</style>
</head>
<body>

<div class="abs service-link" style="top:42px">Clinical Massage</div>
<div class="abs service-link" style="top:68px">Psychotherapy</div>
<div class="abs service-divider"></div>
<div class="abs top-rule"></div>

<h2 class="abs section-title" style="top:153px;font-size:17.5px">Doctors</h2>
<div class="abs title-rule" style="top:186px"></div>
<p class="abs section-sub" style="top:200px">Meet our caring specialists</p>

<div class="abs doctor-card" style="left:151px;top:229px">
  <div class="doctor-photo" role="img" aria-label="Portrait of a smiling male doctor in a white coat" style="background:linear-gradient(160deg,#dbeaf8,#b9d3ec)"></div>
  <div class="doctor-info">
    <div class="doctor-name">Martin Greaves</div>
    <div class="doctor-role">Chief Medical Officer</div>
    <div class="doctor-note" style="margin-top:11px">Lead</div>
    <div class="social"><span></span><span></span><span></span><span></span></div>
  </div>
</div>

<div class="abs doctor-card" style="left:472px;top:229px">
  <div class="doctor-photo" role="img" aria-label="Portrait of a smiling female doctor with a stethoscope" style="background:linear-gradient(160deg,#f4f4f4,#d9dde0)"></div>
  <div class="doctor-info">
    <div class="doctor-name">Clara Whitfield</div>
    <div class="doctor-role">Physician</div>
    <div class="doctor-rule"></div>
    <div class="doctor-note">Internal medicine</div>
    <div class="social"><span></span><span></span><span></span><span></span></div>
  </div>
</div>

<div class="abs doctor-card" style="left:151px;top:378px">
  <div class="doctor-photo" role="img" aria-label="Portrait of a male doctor wearing glasses" style="background:linear-gradient(160deg,#e6e7e8,#bfc3c6)"></div>
  <div class="doctor-info">
    <div class="doctor-name">Daniel Hartley</div>
    <div class="doctor-role">Surgeon</div>
    <div class="doctor-rule"></div>
    <div class="doctor-note">General surgery</div>
    <div class="social"><span></span><span></span><span></span><span></span></div>
  </div>
</div>

<div class="abs doctor-card" style="left:472px;top:378px">
  <div class="doctor-photo" role="img" aria-label="Portrait of a smiling female neurosurgeon" style="background:linear-gradient(160deg,#ececec,#cfd3d6)"></div>
  <div class="doctor-info">
    <div class="doctor-name">Elena Marsh</div>
    <div class="doctor-role">Neurosurgeon</div>
    <div class="doctor-rule"></div>
    <div class="doctor-note">Brain care</div>
    <div class="social"><span></span><span></span><span></span><span></span></div>
  </div>
</div>

<section class="abs faq-band"></section>
<h2 class="abs section-title" style="top:578px;font-size:18px">Frequently Asked Questions</h2>
<div class="abs title-rule" style="top:612px"></div>
<p class="abs section-sub" style="top:626px">Answers to common questions from our patients</p>

<div class="abs faq-item open" style="top:655px;height:54px">
  <div class="faq-q"><svg width="12" height="12" viewBox="0 0 12 12"><circle cx="6" cy="6" r="5.2" fill="none" stroke="#7fb0dd" stroke-width="1"/><path d="M4.6 4.6a1.4 1.4 0 1 1 1.9 1.3c-.4.2-.5.5-.5.9" fill="none" stroke="#7fb0dd" stroke-width="1"/><circle cx="6" cy="8.7" r=".6" fill="#7fb0dd"/></svg>How do I book a consultation?</div>
  <div class="faq-a">Use our free consultation form online.</div>
  <svg class="chev" width="8" height="6" viewBox="0 0 8 6"><path d="M1 4.5 4 1.5 7 4.5" fill="none" stroke="#1977cc" stroke-width="1.3"/></svg>
</div>

<div class="abs faq-item" style="top:718px;height:36px">
  <div class="faq-q"><svg width="12" height="12" viewBox="0 0 12 12"><circle cx="6" cy="6" r="5.2" fill="none" stroke="#7fb0dd" stroke-width="1"/><path d="M4.6 4.6a1.4 1.4 0 1 1 1.9 1.3c-.4.2-.5.5-.5.9" fill="none" stroke="#7fb0dd" stroke-width="1"/><circle cx="6" cy="8.7" r=".6" fill="#7fb0dd"/></svg>Is the first consultation free of charge?</div>
  <svg class="chev" width="8" height="6" viewBox="0 0 8 6"><path d="M1 1.5 4 4.5 7 1.5" fill="none" stroke="#2c4964" stroke-width="1.3"/></svg>
</div>

<div class="abs faq-item" style="top:763px;height:36px">
  <div class="faq-q"><svg width="12" height="12" viewBox="0 0 12 12"><circle cx="6" cy="6" r="5.2" fill="none" stroke="#7fb0dd" stroke-width="1"/><path d="M4.6 4.6a1.4 1.4 0 1 1 1.9 1.3c-.4.2-.5.5-.5.9" fill="none" stroke="#7fb0dd" stroke-width="1"/><circle cx="6" cy="8.7" r=".6" fill="#7fb0dd"/></svg>Which treatments do you offer for back pain?</div>
  <svg class="chev" width="8" height="6" viewBox="0 0 8 6"><path d="M1 1.5 4 4.5 7 1.5" fill="none" stroke="#2c4964" stroke-width="1.3"/></svg>
</div>

<div class="abs faq-item" style="top:808px;height:36px">
  <div class="faq-q"><svg width="12" height="12" viewBox="0 0 12 12"><circle cx="6" cy="6" r="5.2" fill="none" stroke="#7fb0dd" stroke-width="1"/><path d="M4.6 4.6a1.4 1.4 0 1 1 1.9 1.3c-.4.2-.5.5-.5.9" fill="none" stroke="#7fb0dd" stroke-width="1"/><circle cx="6" cy="8.7" r=".6" fill="#7fb0dd"/></svg>Do you accept health insurance plans?</div>
  <svg class="chev" width="8" height="6" viewBox="0 0 8 6"><path d="M1 1.5 4 4.5 7 1.5" fill="none" stroke="#2c4964" stroke-width="1.3"/></svg>
</div>

<div class="abs faq-item" style="top:852px;height:36px">
  <div class="faq-q"><svg width="12" height="12" viewBox="0 0 12 12"><circle cx="6" cy="6" r="5.2" fill="none" stroke="#7fb0dd" stroke-width="1"/><path d="M4.6 4.6a1.4 1.4 0 1 1 1.9 1.3c-.4.2-.5.5-.5.9" fill="none" stroke="#7fb0dd" stroke-width="1"/><circle cx="6" cy="8.7" r=".6" fill="#7fb0dd"/></svg>How long does a typical session last?</div>
  <svg class="chev" width="8" height="6" viewBox="0 0 8 6"><path d="M1 1.5 4 4.5 7 1.5" fill="none" stroke="#2c4964" stroke-width="1.3"/></svg>
</div>

<h2 class="abs section-title" style="top:963px;font-size:18px">Gallery</h2>
<div class="abs title-rule" style="top:997px"></div>
<p class="abs section-sub" style="top:1011px">Inside our clinic</p>

<div class="abs gallery-shot" role="img" aria-label="Surgical team in green scrubs under operating lights" style="left:39px;width:211px;background:linear-gradient(135deg,#c9d8dd,#2aa39a 60%,#137a72)"></div>
<div class="abs gallery-shot" role="img" aria-label="Gloved hand handling a test tube beside lab equipment" style="left:252px;width:210px;background:linear-gradient(135deg,#d9d4cf,#f0ede8 55%,#9a9896)"></div>
<div class="abs gallery-shot" role="img" aria-label="Researcher in a white coat working in a laboratory" style="left:463px;width:211px;background:linear-gradient(135deg,#b9c4cc,#e4e8eb 50%,#8a9aa6)"></div>
<div class="abs gallery-shot" role="img" aria-label="Surgeons in blue gowns performing an operation" style="left:676px;width:211px;background:linear-gradient(135deg,#7a9cc4,#3f6da8 55%,#c9d3e6)"></div>

</body>
</html>
```